Artwork-Design (Cover) für Musikalbum
Zielgruppe
Wir sind eine Tonträgerfirma und bewegen uns im Low-Budget-Segment.
Aufgabenstellung
Artwork-Design (Cover) für ein Musikalbum : 'Songs From The Prairie'
Wir benötigen nicht das komplette Artwork, sondern ein Frontcover
(121 x 120 mm + 20 mm Beschnitt) wg. etwaiger Verschiebung der Positionierung.
Fertigstellung (Aufziehen des Inlays und Labels) erfolgt später bei uns im Hause.
Wir benötigen später eine offene psd-Datei mit allen Ebenen.
Wichtig: Schriften nicht gerastert ggfs. Schrift mitliefern.
Was wir uns vorstellen:
- Entsprechend der Musik Bild, Tracks Beispiele:
-HALF A MOONLIGHT - TALWIND
-FARMYARD LADY IN A GREY MOOD - MERRIT, ODESSA P
-MAGGIE PLEASE COME BACK TO THE HOLLOW - BAXLEY, ORVAL
-PORTRAIT OF A DRIFTER - HOLTZ, WADE
- Bildmaterial sollte bei bildwerkpool, lumarchiv oder p-depot ausgesucht werden, das Bildmaterial wird dann später auch von uns dort eingekauft.
- keine Künstlerfotos.
Wir freuen uns und sind sehr gespannt auf eure Vorschläge,
bei Fragen gerne mailen

```html
<!DOCTYPE html>
<html lang="de">
<head>
<meta charset="utf-8">
<title>Songs From The Prairie – Frontcover</title>
<link rel="stylesheet" href="https://fonts.googleapis.com/css2?family=Alfa+Slab+One&display=swap">
<style>
  :root {
    --ink: #0b0b0b;
    --white: #ffffff;
    --amber: #f0a01e;
    --frame: #e4e4e4;
  }
  html, body {
    margin: 0;
    padding: 0;
    width: 1200px;
    height: 1189px;
    overflow: hidden;
    background: var(--ink);
  }
  .cover {
    position: relative;
    width: 1200px;
    height: 1189px;
    overflow: hidden;
  }
  .cover-art {
    position: absolute;
    inset: 0;
    width: 1200px;
    height: 1189px;
  }
  .title {
    position: absolute;
    margin: 0;
    font-family: "Alfa Slab One", Georgia, serif;
    font-weight: 400;
    text-align: center;
    white-space: nowrap;
    transform: skewX(-12deg);
    line-height: 1;
  }
  .title-main {
    top: 448px;
    left: 360px;
    width: 700px;
    font-size: 158px;
    color: var(--white);
    letter-spacing: 1px;
  }
  .title-sub {
    top: 640px;
    left: 284px;
    width: 722px;
    font-size: 60px;
    color: var(--amber);
    letter-spacing: 3px;
  }
  .tracklist {
    position: absolute;
    top: 826px;
    left: 190px;
    width: 800px;
    margin: 0;
    padding: 0;
    list-style: none;
    text-align: center;
    font-family: "Alfa Slab One", Georgia, serif;
    font-weight: 400;
    letter-spacing: 2px;
    white-space: nowrap;
  }
  .track {
    font-size: 27px;
    line-height: 43px;
    color: var(--white);
  }
  .track--highlight { color: var(--amber); }
  .track--label {
    font-size: 14px;
    line-height: 40px;
    color: var(--amber);
    letter-spacing: 3px;
  }
</style>
</head>
<body>
<main class="cover">
  <svg class="cover-art" viewBox="0 0 1200 1189" xmlns="http://www.w3.org/2000/svg">
    <defs>
      <linearGradient id="photo-base" x1="0" y1="0" x2="1" y2="0.6">
        <stop offset="0" stop-color="#3d5a45"/>
        <stop offset="0.45" stop-color="#7a5a30"/>
        <stop offset="0.75" stop-color="#c8742a"/>
        <stop offset="1" stop-color="#5a3016"/>
      </linearGradient>
      <radialGradient id="shirt-tone" cx="0.18" cy="0.55" r="0.4">
        <stop offset="0" stop-color="#5f8a62"/>
        <stop offset="1" stop-color="#5f8a62" stop-opacity="0"/>
      </radialGradient>
      <radialGradient id="glow-tone" cx="0.78" cy="0.3" r="0.32">
        <stop offset="0" stop-color="#f0a040"/>
        <stop offset="1" stop-color="#f0a040" stop-opacity="0"/>
      </radialGradient>
      <radialGradient id="shade-tone" cx="0.5" cy="0.18" r="0.22">
        <stop offset="0" stop-color="#1c1610" stop-opacity="0.85"/>
        <stop offset="1" stop-color="#1c1610" stop-opacity="0"/>
      </radialGradient>
      <radialGradient id="skin-tone" cx="0.4" cy="0.28" r="0.16">
        <stop offset="0" stop-color="#c98a5a" stop-opacity="0.8"/>
        <stop offset="1" stop-color="#c98a5a" stop-opacity="0"/>
      </radialGradient>
      <linearGradient id="wood-tone" x1="0" y1="0" x2="1" y2="0">
        <stop offset="0" stop-color="#5a4630"/>
        <stop offset="0.4" stop-color="#a8906a"/>
        <stop offset="0.7" stop-color="#6e5638"/>
        <stop offset="1" stop-color="#8f7652"/>
      </linearGradient>
      <linearGradient id="panel-tone" x1="0" y1="0" x2="0" y2="1">
        <stop offset="0" stop-color="#000" stop-opacity="0.95"/>
        <stop offset="0.7" stop-color="#000" stop-opacity="0.85"/>
        <stop offset="1" stop-color="#000" stop-opacity="0.55"/>
      </linearGradient>
    </defs>

    <g class="photo-area" role="img" aria-label="Stimmungsfoto: Cowboy mit Hut und Sonnenbrille in warmem Abendlicht">
      <rect width="1200" height="1189" fill="url(#photo-base)"/>
      <rect width="1200" height="1189" fill="url(#shirt-tone)"/>
      <rect width="1200" height="1189" fill="url(#glow-tone)"/>
      <rect width="1200" height="1189" fill="url(#skin-tone)"/>
      <rect width="1200" height="1189" fill="url(#shade-tone)"/>
    </g>

    <g class="wood-frame" role="img" aria-label="Verwitterte Holzbretter als Rahmen oben und unten">
      <path d="M0,0 H1200 V130 C1080,130 1060,70 900,70 H360 C200,70 150,140 0,140 Z" fill="url(#wood-tone)"/>
      <path d="M0,1010 C150,1010 250,1060 400,1060 H800 C950,1060 1050,1000 1200,1000 V1189 H0 Z" fill="url(#wood-tone)"/>
    </g>

    <path class="title-panel" d="M470,430 H1200 V1000 C1050,1000 950,1060 800,1060 H400 C300,1060 240,1040 200,1030 L215,780 L275,705 Z" fill="url(#panel-tone)"/>

    <g class="frame-lines" fill="none" stroke="var(--frame)" stroke-width="7" opacity="0.85">
      <path d="M0,140 C150,140 200,70 360,70 H900 C1060,70 1080,130 1200,130"/>
      <path d="M0,1010 C150,1010 250,1060 400,1060 H800 C950,1060 1050,1000 1200,1000"/>
    </g>

    <g class="divider" fill="var(--white)">
      <circle cx="372" cy="760" r="5"/><circle cx="405" cy="760" r="5"/><circle cx="438" cy="760" r="5"/><circle cx="471" cy="760" r="5"/><circle cx="504" cy="760" r="5"/>
      <circle cx="664" cy="760" r="5"/><circle cx="697" cy="760" r="5"/><circle cx="730" cy="760" r="5"/><circle cx="763" cy="760" r="5"/><circle cx="796" cy="760" r="5"/>
      <rect x="525" y="759" width="120" height="2" fill="var(--amber)"/>
      <circle cx="585" cy="760" r="5"/>
    </g>
  </svg>

  <h1 class="title title-main">SONGS</h1>
  <p class="title title-sub">FROM THE PRAIRIE</p>

  <ul class="tracklist">
    <li class="track">FARMYARD LADY IN A GREY MOOD</li>
    <li class="track track--highlight">PORTRAIT OF A DRIFTER</li>
    <li class="track">HALF A MOONLIGHT</li>
    <li class="track track--label">MOORFELD RECORDS</li>
  </ul>
</main>
</body>
</html>
```